Kovala RQNV Magazine Cover style graphic.

I am looking to create a document cover.
Brantley Solutions
The True Cost of an Embroidery Machineā€
Subtitle: Why the Lowest Upfront Price Can Become the Most Expensive Decision. Using Brantley logo's and Kovala RQNV for a high impact cover. It should look like a magazine cover. This is the most advance technology available for the embroidery industry. We want to portray this as a platform and not simply a machine. We will have an 8 page guide.

Target Market(s)

Our customer base

Industry/Entity Type

Industrial Embroidery

Font styles to use
Serif

Colors
0054AA
0677BA
7BADD7
CADEEF
E8F1F8

Requirements
Must have
• High impact, visually pleasing cover.

```html
<!DOCTYPE html>
<html lang="en">
<head>
<meta charset="utf-8">
<title>Brantley Solutions – The True Cost of an Embroidery Machine</title>
<link href="https://fonts.googleapis.com/css2?family=Poppins:wght@500;600;700&display=swap" rel="stylesheet">
<style>
  :root {
    --ink-black: #000000;
    --navy-deep: #0a2a55;
    --navy-glow: #0b3a78;
    --accent-blue: #2196dc;
    --text-white: #ffffff;
    --machine-light: #d9dde2;
    --machine-mid: #9aa3ad;
    --garment-purple: #5a2fa0;
  }
  html, body {
    margin: 0;
    padding: 0;
    width: 980px;
    height: 1200px;
    overflow: hidden;
    background: var(--ink-black);
  }
  .cover {
    position: relative;
    width: 980px;
    height: 1200px;
    overflow: hidden;
    font-family: "Poppins", sans-serif;
    color: var(--text-white);
    background:
      radial-gradient(ellipse 520px 520px at 700px 560px, rgba(11, 58, 120, 0.75), rgba(0, 0, 0, 0) 70%),
      linear-gradient(160deg, var(--navy-deep) 0%, #02101f 28%, var(--ink-black) 50%, #010712 100%);
  }
  .brand {
    position: absolute;
    left: 75px;
    top: 66px;
    display: flex;
    align-items: center;
    gap: 12px;
  }
  .brand-square {
    width: 98px;
    height: 98px;
    background: var(--accent-blue);
  }
  .brand-name {
    font-weight: 700;
    font-size: 43px;
    line-height: 44px;
    color: var(--text-white);
    letter-spacing: -0.5px;
  }
  .hero-photo {
    position: absolute;
    left: 353px;
    top: 283px;
    width: 627px;
    height: 917px;
    background:
      radial-gradient(ellipse 200px 230px at 230px 820px, rgba(90, 47, 160, 0.85), rgba(90, 47, 160, 0) 75%),
      radial-gradient(ellipse 260px 420px at 360px 360px, rgba(217, 221, 226, 0.85), rgba(154, 163, 173, 0.35) 65%, rgba(0, 0, 0, 0) 100%);
  }
  .title {
    position: absolute;
    left: 75px;
    top: 312px;
    margin: 0;
    font-weight: 600;
    font-size: 64px;
    line-height: 68px;
    letter-spacing: -0.5px;
  }
  .title .highlight { color: var(--accent-blue); }
  .title-rule {
    position: absolute;
    left: 77px;
    top: 603px;
    width: 75px;
    height: 10px;
    border-radius: 5px;
    background: var(--accent-blue);
  }
  .subtitle {
    position: absolute;
    left: 75px;
    top: 640px;
    margin: 0;
    font-weight: 500;
    font-size: 24px;
    line-height: 33px;
  }
  .platform-mark {
    position: absolute;
    left: 75px;
    top: 1038px;
    display: flex;
    align-items: center;
    gap: 10px;
  }
  .platform-square {
    width: 20px;
    height: 20px;
    background: var(--accent-blue);
  }
  .platform-name {
    font-weight: 700;
    font-size: 46px;
    line-height: 60px;
    color: var(--text-white);
  }
</style>
</head>
<body>
  <main class="cover">
    <div class="hero-photo" role="img" aria-label="Photo of a white multi-needle industrial embroidery machine with thread cones and a control screen, stitching a purple shirt on its hoop"></div>

    <header class="brand">
      <div class="brand-square"></div>
      <div class="brand-name">BRANTLEY<br>SOLUTIONS</div>
    </header>

    <h1 class="title">The True<br>Cost of an<br><span class="highlight">Embroidery</span><br>Machine</h1>
    <div class="title-rule"></div>
    <p class="subtitle">Why the Lowest<br>Upfront Price Can<br>Become the Most<br>Expensive Decision</p>

    <footer class="platform-mark">
      <span class="platform-name">q-NX</span>
      <span class="platform-square"></span>
    </footer>
  </main>
</body>
</html>
```